ASL Learning Website Application Pages Redesign

Introduction:
We need a redesign of the internal pages of our website, SignTrellis.com. The current website design has been in place for many years and is not mobile friendly. We want an updated design that makes the site look cleaner, more professional, and mobile accessible. We are looking for a design that eliminates the clutter on each page, and makes the site simple and easy to use. We will be interested in your design if it is unique and creative. Don't be afraid to completely change the look of the site.

We need the designs sliced up into clean HTML files that are responsive and work well on both mobile and desktop computers. We will implement the PHP needed to make the pages functional.

About Us:
SignTrellis is a subscription-based website for American Sign Language (ASL) video lessons. The content is for anyone who wishes to learn ASL, regardless of age. It has been designed to instruct Deaf students, parents of Deaf children, and the community-at-large. All lessons are taught by Deaf experts of ASL.

Overview:
The website before log-in does not need any changes. There are five key pages within the internal website (after log-in) that need to be redesigned; they are listed below. Note that some pages (Dictionary and Activity) have multiple sub-pages, so there are about 6-8 pages in total to design, depending on how you decide to approach this (more info in the pages’ respective instruction documents).

The new page designs should retain their existing features, and as stated before, should be mobile friendly. However, you may combine, collapse, or completely change the look of these features. Each page to redesign has a separate instruction document attachment, and screenshots of the current version of the page. Our logo has also been attached. If you want to see the website pages for yourself, you can also go to our website (SignTrellis.com) and use a free trial to get access to the internal site.

As for design preferences, we want our site to be modern-looking and mature. We’re looking for an inviting, educational style that can attract both high school students and adults. We’re happy with the current font and color scheme, but we’re always open to ideas!

Additional Notes:
- Every page has the same header and footer. You could keep these the same, or change them, based on your discretion.
- Currently, every page also has a breadcrumb. The breadcrumb is unnecessary and you may remove it. However, the “add/remove from favorites” button on the right of the breadcrumb is necessary to keep somewhere on the page.

Pages:
Here’s a list of the five key pages we need redesigned:
- Dashboard
- Dictionary
- Lesson
- Activity
- All Lessons

Each page has its own instruction document. These are attached separately.

Just purchased a $150 for Top designers. I need to give them time to submit their designs . Can I have 7 more days?

Target Market(s)

Deaf students, parents of Deaf children, and the community-at-large interested in learning ASL

Coding

Coded - Design and coding required

Number of Pages Required

5+ page

Font styles to use
Sans Serif

Requirements
Must have
• Responsive design - the full application experience should be available on mobile devices.
Follow the directions on the design brief.
Nice to have
• Be creative! Please play around with, or even completely change, the look of the site.

```html
<!DOCTYPE html>
<html lang="en">
<head>
<meta charset="utf-8">
<title>SignTrellis – Dashboard</title>
<link rel="stylesheet" href="https://fonts.googleapis.com/css2?family=Montserrat:wght@500;600;700&family=Roboto:wght@400;500;700&display=swap">
<style>
:root{
  --green:#4fd25a;
  --green-2:#5bd97e;
  --green-text:#3cc43f;
  --orange:#f39a33;
  --red:#e53935;
  --ink:#111;
  --text:#222;
  --muted:#555;
  --page:#f4f4f4;
  --card:#fff;
  --line:#e6e6e6;
}
*{box-sizing:border-box;margin:0;padding:0}
html,body{width:1200px;height:2452px;overflow:hidden}
body{background:var(--page);font-family:'Roboto',sans-serif;color:var(--text);font-size:15px}
a{color:inherit;text-decoration:none}
.wrap{width:980px;margin:0 auto}

/* header */
.site-header{height:76px;background:#fff;border-bottom:3px solid var(--green)}
.site-header .wrap{display:flex;align-items:center;height:73px}
.brand{display:flex;align-items:center;gap:8px;font-family:'Roboto',sans-serif;font-weight:700;font-size:24px;color:#2b2b2b}
.brand-dot{width:14px;height:14px;border-radius:50%;background:var(--green)}
.main-nav{display:flex;gap:32px;margin-left:40px;font-size:15.5px;color:#222}
.main-nav a.active{color:var(--green-text)}
.main-nav .caret{display:inline-block;width:8px;height:8px;border-right:1.6px solid #222;border-bottom:1.6px solid #222;transform:rotate(45deg);margin-left:6px;position:relative;top:-3px}
.avatar{margin-left:auto;width:44px;height:44px;border-radius:50%;background:var(--green);color:#fff;font-family:'Montserrat',sans-serif;font-weight:700;font-size:20px;display:flex;align-items:center;justify-content:center}

/* welcome */
.welcome{display:flex;justify-content:space-between;align-items:flex-start;padding-top:36px;height:136px}
.welcome h1{font-family:'Montserrat',sans-serif;font-weight:700;font-size:38px;color:var(--ink);line-height:1}
.welcome .toggle{display:block;color:var(--orange);font-size:15px;margin-top:12px}
.btn-outline{border:2px solid var(--green);border-radius:5px;padding:10px 18px;font-size:15px;background:#fff;color:#222;margin-top:-3px}

/* cards */
.card{background:var(--card);border-radius:6px;box-shadow:0 2px 8px rgba(0,0,0,.06);margin-bottom:20px;overflow:hidden}
.card-head{height:62px;background:linear-gradient(90deg,var(--green),var(--green-2));display:flex;align-items:center;justify-content:space-between;padding:0 36px;border-bottom:3px solid #e2e2e2}
.card-head h2{font-family:'Montserrat',sans-serif;font-weight:600;font-size:25px;color:#111}
.card-head .more{font-family:'Montserrat',sans-serif;font-weight:500;font-size:16px;color:#111}
.dots{display:flex;flex-direction:column;gap:4px}
.dots i{width:5px;height:5px;border-radius:50%;background:#111;display:block}

/* my pages */
.shortcuts{display:flex;padding:24px 0 28px 0}
.shortcut{width:132px;text-align:center;font-size:14px;font-weight:500;color:#111}
.shortcut svg{display:block;margin:0 auto 12px;height:52px}

/* lessons */
.next{display:flex;margin:0 36px;padding:36px 0 24px;border-bottom:2px solid var(--line)}
.next > div{flex:1;text-align:center;min-height:132px}
.next > div+div{border-left:2px solid var(--line)}
.next .label{font-family:'Montserrat',sans-serif;font-weight:500;font-size:19px;color:#111}
.next .value{font-family:'Roboto',sans-serif;font-weight:700;font-size:30px;color:var(--orange);margin-top:18px;line-height:1.05}
.lesson-row{display:flex;gap:30px;padding:38px 36px 36px}
.lesson{width:149px;height:229px;border:1.5px solid #e2e2e2;border-radius:5px;overflow:hidden;box-shadow:0 2px 5px rgba(0,0,0,.08)}
.lesson .thumb{height:104px}
.lesson h3{font-weight:500;font-size:20px;color:#111;padding:8px 8px 0;line-height:1.15;min-height:56px}
.lesson h3.two{min-height:56px}
.tag{display:inline-block;background:var(--green);color:#111;font-size:11.5px;font-weight:500;border-radius:10px;padding:3px 9px;margin:0 0 6px 8px}
.tags{display:flex;flex-direction:column;align-items:flex-start}

/* progress */
.progress{padding:30px 36px 36px}
.progress-cols,.progress-row{display:grid;grid-template-columns:100px 145px 225px 75px 110px 1fr;align-items:center}
.progress-cols{font-family:'Montserrat',sans-serif;font-weight:500;font-size:20px;color:#111;padding:0 0 18px 26px}
.progress-row{height:52px;background:#fff;border-left:8px solid var(--green);border-radius:4px;box-shadow:0 1px 6px rgba(0,0,0,.1);margin-bottom:10px;padding-left:18px;font-size:15.5px;color:#222}
.progress-row .opts{color:var(--orange)}
.progress-row .opts span{color:#222}

/* requested words */
.requests{display:flex;margin:0 36px;padding:38px 0 28px;border-bottom:2px solid var(--line)}
.requests > div{flex:1;text-align:center;min-height:104px}
.requests > div+div{border-left:2px solid var(--line)}
.requests .label{font-family:'Montserrat',sans-serif;font-weight:500;font-size:20px;color:#111}
.requests .count{font-family:'Montserrat',sans-serif;font-weight:700;font-size:38px;margin-top:14px}
.count.pending{color:var(--red)}
.count.done{color:var(--green-text)}
.request-form{padding:22px 36px 34px;font-size:19px;color:#111}
.field-line{display:flex;align-items:center;gap:12px;margin:18px 0 24px}
.input{border:2px solid var(--green);border-radius:3px;height:52px;display:flex;align-items:center;padding:0 18px;color:#777;font-size:19px;background:#fff}
.input.word{width:352px}
.input.full{width:100%;margin-top:16px}
.btn-request{display:inline-block;margin-top:36px;padding:15px 33px;font-family:'Montserrat',sans-serif;font-weight:600;font-size:20px;color:var(--green-text);background:#fff;border-radius:4px;box-shadow:0 2px 8px rgba(0,0,0,.15)}

/* footer */
.site-footer{background:#fff;border-top:3px solid var(--green);margin-top:36px;height:360px}
.footer-top{display:flex;padding-top:40px;height:272px;border-bottom:2px solid var(--green)}
.footer-brand{width:296px;padding-top:72px;display:flex;align-items:center;gap:10px;font-weight:700;font-size:38px;color:#2b2b2b;align-self:flex-start}
.footer-brand .brand-dot{width:22px;height:22px}
.footer h4,.site-footer h4{font-family:'Montserrat',sans-serif;font-weight:500;font-size:20px;color:#111;margin-bottom:12px}
.quick{width:350px}
.quick ul{list-style:none;display:grid;grid-template-columns:134px 1fr;grid-auto-flow:column;grid-template-rows:repeat(5,33px);font-size:15.5px;color:#222}
.contact ul{list-style:none;font-size:15.5px;color:#222}
.contact li{display:flex;align-items:center;gap:24px;height:36px}
.contact svg{width:20px;height:20px}
.footer-bottom{display:flex;justify-content:space-between;align-items:center;height:86px;font-size:15.5px;color:#222}
.socials{display:flex;gap:12px}
.socials span{width:44px;height:44px;border:2px solid var(--green);border-radius:50%}
</style>
</head>
<body>

<header class="site-header">
  <div class="wrap">
    <a class="brand" href="#"><span class="brand-dot"></span>SignTrellis</a>
    <nav class="main-nav">
      <a class="active" href="#">Dashboard</a>
      <a href="#">Lessons<span class="caret"></span></a>
      <a href="#">Lesson List</a>
      <a href="#">Dictionary</a>
      <a href="#">Handshapes<span class="caret"></span></a>
      <a href="#">Locations<span class="caret"></span></a>
      <a href="#">Blog</a>
    </nav>
    <div class="avatar">S</div>
  </div>
</header>

<main class="wrap">
  <section class="welcome">
    <div>
      <h1>Welcome Marlowe</h1>
      <a class="toggle" href="#">Show Welcome Message &rsaquo;</a>
    </div>
    <a class="btn-outline" href="#">Add To Favorites</a>
  </section>

  <section class="card">
    <div class="card-head"><h2>My Pages</h2></div>
    <div class="shortcuts">
      <a class="shortcut" href="#" style="margin-left:14px">
        <svg viewBox="0 0 64 52" width="64"><g fill="none" stroke="#f39a33" stroke-width="4"><path d="M4 8h22l6 4 6-4h22v40H38l-6 3-6-3H4z"/><path d="M32 12v38"/><path d="M10 8v34h16M54 8v34H38"/></g></svg>Dictionary</a>
      <a class="shortcut" href="#">
        <svg viewBox="0 0 52 52" width="52"><path d="M4 4h44v12h-4l-2-6H31v36h7v4H14v-4h7V10H10l-2 6H4z" fill="#f39a33"/></svg>My Vocabulary</a>
      <a class="shortcut" href="#">
        <svg viewBox="0 0 46 52" width="46"><g fill="none" stroke="#f39a33" stroke-width="3.5"><path d="M10 3h32v40l-8 7H10z"/><path d="M4 10v40h30"/><path d="M17 14h18M17 22h18M17 30h12"/></g></svg>Favorites</a>
      <a class="shortcut" href="#">
        <svg viewBox="0 0 52 52" width="52"><circle cx="26" cy="26" r="23" fill="none" stroke="#f39a33" stroke-width="3.5"/><circle cx="28" cy="15" r="3" fill="#f39a33"/><path d="M22 23h7l-4 15h6" fill="none" stroke="#f39a33" stroke-width="3.5"/></svg>Tips and Grammar</a>
      <a class="shortcut" href="#">
        <svg viewBox="0 0 56 52" width="56"><g fill="none" stroke="#f39a33" stroke-width="3.5"><rect x="21" y="3" width="14" height="10"/><rect x="4" y="38" width="12" height="10"/><rect x="22" y="38" width="12" height="10"/><rect x="40" y="38" width="12" height="10"/><path d="M28 13v12M10 38V26h36v12M28 25v13"/></g></svg>Multiple Meanings</a>
      <a class="shortcut" href="#">
        <svg viewBox="0 0 52 52" width="52"><g fill="none" stroke="#f39a33" stroke-width="3.5"><rect x="4" y="4" width="44" height="44"/><path d="M4 12h44M12 22h28M12 30h28M12 38h28"/></g></svg>Lesson List</a>
      <a class="shortcut" href="#">
        <svg viewBox="0 0 52 52" width="52"><circle cx="26" cy="26" r="23" fill="none" stroke="#f39a33" stroke-width="3.5"/><path d="M26 12l4 9 10 1-7.5 6.5 2.3 9.8L26 33l-8.8 5.3 2.3-9.8L12 22l10-1z" fill="#f39a33"/></svg>My Lessons</a>
    </div>
  </section>

  <section class="card">
    <div class="card-head"><h2>Lessons</h2><a class="more" href="#">More Lessons &rsaquo;</a></div>
    <div class="next">
      <div><div class="label">Next Lesson :</div><div class="value">Alphabets</div></div>
      <div><div class="label">Next Activity :</div><div class="value">Choose the<br>Correct Sentence</div></div>
    </div>
    <div class="lesson-row">
      <article class="lesson">
        <div class="thumb" role="img" aria-label="Streaks of rainbow paint" style="background:linear-gradient(90deg,#e8a020,#e53935,#c2185b,#7b1fa2,#1e88e5,#43a047,#1a237e)"></div>
        <h3>Colors</h3><div class="tags"><span class="tag">Beginner</span></div>
      </article>
      <article class="lesson">
        <div class="thumb" role="img" aria-label="Person resting beside a campfire on a rocky shore" style="background:linear-gradient(180deg,#b8bcbf,#7d7f7c 55%,#3b3a36)"></div>
        <h3>Survival Words</h3><div class="tags"><span class="tag">Beginner</span></div>
      </article>
      <article class="lesson">
        <div class="thumb" role="img" aria-label="Question mark drawn on textured paper" style="background:linear-gradient(135deg,#c8a98a,#b99474)"></div>
        <h3>Deaf Culture 1</h3><div class="tags"><span class="tag">Beginner</span><span class="tag">Deaf Culture</span></div>
      </article>
      <article class="lesson">
        <div class="thumb" role="img" aria-label="Hand forming a fingerspelled letter" style="background:linear-gradient(135deg,#f2f2f2,#e6d3c6)"></div>
        <h3 class="two">Fingerspelling 1</h3><div class="tags"><span class="tag">Beginner</span><span class="tag">Fingerspelling</span></div>
      </article>
      <article class="lesson">
        <div class="thumb" role="img" aria-label="Parent and child together at home" style="background:linear-gradient(135deg,#d9d9d9,#8a6a55 60%,#efefef)"></div>
        <h3>Family</h3><div class="tags"><span class="tag">Beginner</span></div>
      </article>
    </div>
  </section>

  <section class="card">
    <div class="card-head"><h2>Your Progress</h2><div class="dots"><i></i><i></i><i></i></div></div>
    <div class="progress">
      <div class="progress-cols"><span>Date</span><span>Lesson</span><span>Activity</span><span>Score</span><span>Attempts</span><span>Options</span></div>
      <div class="progress-row"><span>05/21/2021</span><span>Colors</span><span>Match the vocabulary</span><span>100%</span><span>1</span><span class="opts">Review Lesson<span>,</span> Retry Activity</span></div>
      <div class="progress-row"><span>05/21/2021</span><span>Numbers 1-20</span><span>Grammar instruction</span><span>100%</span><span>1</span><span class="opts">Review Lesson<span>,</span> Retry Activity</span></div>
      <div class="progress-row"><span>05/21/2021</span><span>Numbers 1-20</span><span>Do these video match?</span><span>100%</span><span>1</span><span class="opts">Review Lesson<span>,</span> Retry Activity</span></div>
      <div class="progress-row"><span>05/21/2021</span><span>Meet &amp; Greet</span><span>Choose the correct location</span><span>100%</span><span>1</span><span class="opts">Review Lesson<span>,</span> Retry Activity</span></div>
      <div class="progress-row"><span>05/21/2021</span><span>Meet &amp; Greet</span><span>English to ASL Practice</span><span>100%</span><span>1</span><span class="opts">Review Lesson<span>,</span> Retry Activity</span></div>
    </div>
  </section>

  <section class="card">
    <div class="card-head"><h2>Requested Words</h2></div>
    <div class="requests">
      <div><div class="label">Pending Requests :</div><div class="count pending">0</div></div>
      <div><div class="label">Completed Requests :</div><div class="count done">15</div></div>
    </div>
    <form class="request-form">
      <p>Can’t find the word you’re looking for? Use the form below to request that we add it to our dictionary.</p>
      <div class="field-line">Word to add : <div class="input word">Write a word</div></div>
      <p>Sample sentence or definition of the word to give us context so we can properly sign your word.</p>
      <div class="input full">Sample sentence or definition of the word</div>
      <a class="btn-request" href="#">Request Word</a>
    </form>
  </section>
</main>

<footer class="site-footer">
  <div class="wrap">
    <div class="footer-top">
      <div class="footer-brand"><span class="brand-dot"></span>SignTrellis</div>
      <div class="quick">
        <h4>Quick Link</h4>
        <ul>
          <li>Home</li><li>Try it Free</li><li>Contact Us</li><li>About Us</li><li></li>
          <li>Group Rate Form</li><li>Teacher Guide</li><li>Gift Certificates</li><li>FAQs</li><li>Privacy Policy</li>
        </ul>
      </div>
      <div class="contact">
        <h4>Contact Us</h4>
        <ul>
          <li><svg viewBox="0 0 20 20"><path d="M2 5l5-2 6 2 5-2v12l-5 2-6-2-5 2z M7 3v12M13 5v12" fill="none" stroke="#222" stroke-width="1.6"/></svg>PO Box 5520, Cedar Falls, MI 48000</li>
          <li><svg viewBox="0 0 20 20"><path d="M5 2l3 4-2 2c1 2 3 4 5 5l2-2 4 3-2 3C9 17 3 11 2 5z" fill="#222"/></svg>(555) 014-2278</li>
          <li><svg viewBox="0 0 20 20"><rect x="2" y="4" width="16" height="12" fill="none" stroke="#222" stroke-width="1.8"/><path d="M2 4l8 7 8-7" fill="none" stroke="#222" stroke-width="1.8"/></svg>info@signtrellis.com</li>
        </ul>
      </div>
    </div>
    <div class="footer-bottom">
      <span>Copyrights © 2021, SignTrellis. All rights reserved. Terms &amp; Conditions</span>
      <div class="socials" aria-label="Social links"><span></span><span></span><span></span><span></span><span></span></div>
    </div>
  </div>
</footer>

</body>
</html>
```